Lawn Company needs design work on a service call flyer!

We are a lawn care company that fertilizes and sprays lawns. This design is meant to be left behind at the customers house after a lawn application has been done too let them know what we have done.

The finished design will be printed on A6 paper (4.1 x 5.8 inches)

I have attached PDF files of the text that I want on the front of the document and the back of the document. I also included a sample design that I had been working on to give some idea what I would like. I don't want the same design, but you can use it as a building block for something new or come up with something entirely different.

FRONT: The front of the design is most important.

BACK: Other then the text the design should be minimal. If possible I would like an outline of the trees in my logo to be a backdrop. I have attached a PDF of the back of my business card as an example

The winning design will be a professional looking document that flows and reflects a lawn care business. Please contact me if you have any questions. I will only pick a design that is better then my current template.

Thank You

Target Market(s)

Lawn Care Customers

Industry/Entity Type

Lawn Care

Requirements
Must have
• 1. Our Logo
• 2. The attached text for the front & back of document
• 3. Our phone number (604-918-4471)
• 4. Our Email address (fenwickturfcare@mailora.net)
Nice to have
• A green theme with flowing graphics
Should not have
• any pictures of houses, people, or tools
• Don't copy the text or design from my design template. It is outdated, is it meant to be an example only

```html
<!DOCTYPE html>
<html lang="en">
<head>
<meta charset="utf-8">
<title>Fenwick Turf Care – Service Call Flyer</title>
<link href="https://fonts.googleapis.com/css2?family=Mulish:wght@400;600;700;800;900&display=swap" rel="stylesheet">
<style>
  :root {
    --backdrop: #2c4a33;
    --leaf: #3f8f2a;
    --leaf-deep: #2e6b1f;
    --lime: #9fcf3a;
    --lime-soft: #d9eeb0;
    --paper: #f6fbef;
    --ink: #2c3a25;
    --ink-soft: #5b6652;
    --forest: #1f4a1e;
    --cream: #f1ecb0;
    --sky-top: #8fb6e6;
    --sky-low: #f2e9b4;
    --grass: #5da52b;
  }
  * { box-sizing: border-box; margin: 0; padding: 0; }
  html, body { width: 1200px; height: 800px; overflow: hidden; }
  body {
    background: var(--backdrop);
    font-family: "Mulish", Arial, sans-serif;
    position: relative;
  }
  .card {
    position: absolute;
    top: 209px;
    width: 540px;
    height: 382px;
    overflow: hidden;
  }
  /* ---------- Front ---------- */
  .front {
    left: 40px;
    background: linear-gradient(160deg, var(--paper) 0%, #eef7de 40%, var(--lime-soft) 70%, var(--lime) 100%);
    color: var(--ink);
  }
  .front-art {
    position: absolute; inset: 0;
    background:
      radial-gradient(ellipse 420px 160px at 80% 60%, rgba(159,207,58,.45), transparent 70%),
      radial-gradient(ellipse 200px 260px at 0% 70%, rgba(93,165,43,.55), transparent 70%);
  }
  .grass-strip {
    position: absolute; left: 0; right: 0; bottom: 0; height: 70px;
    background: linear-gradient(180deg, rgba(93,165,43,0) 0%, var(--grass) 35%, var(--leaf-deep) 100%);
  }
  .brand {
    position: absolute; left: 22px; top: 36px;
    display: flex; align-items: center; gap: 8px;
  }
  .brand-dot { width: 20px; height: 20px; border-radius: 50%; background: var(--leaf); }
  .brand-name {
    font-weight: 900; font-size: 24px; line-height: 0.95;
    color: var(--leaf); text-transform: uppercase; letter-spacing: .5px;
  }
  .service-stamp {
    position: absolute; right: 22px; top: 20px; width: 250px;
    text-align: right;
  }
  .stamp-date {
    font-size: 8.5px; text-transform: uppercase; letter-spacing: .3px;
    display: flex; justify-content: flex-end; align-items: flex-end; gap: 4px;
  }
  .fill-line { display: inline-block; border-bottom: 1px solid var(--ink); height: 10px; }
  .stamp-date .fill-line { width: 104px; }
  .stamp-title {
    margin-top: 10px; font-weight: 800; font-size: 12.5px; line-height: 1.3;
    text-transform: uppercase;
  }
  .stamp-by { display: flex; align-items: flex-end; gap: 4px; font-weight: 800; font-size: 12.5px; }
  .stamp-by .fill-line { flex: 1; }
  .application-panel {
    position: absolute; left: 12px; right: 14px; top: 96px; height: 222px;
    background: rgba(255,255,255,.55);
    border-radius: 16px;
    padding: 16px 26px 0;
  }
  .panel-title { text-align: center; font-weight: 800; font-size: 13px; margin-bottom: 10px; }
  .treatment-list { list-style: none; }
  .treatment {
    display: flex; align-items: flex-start; gap: 8px;
    font-size: 12.5px; margin-bottom: 7px;
  }
  .check-box {
    flex: none; width: 16px; height: 16px; margin-top: 1px;
    border: 1.5px solid var(--ink-soft); background: #fff; border-radius: 2px;
  }
  .treatment-note { display: block; font-size: 10px; color: var(--ink-soft); }
  .treatment-other { display: flex; align-items: flex-end; }
  .treatment-other .fill-line { width: 320px; margin: 0 4px; }
  .watering-note { font-size: 12.5px; margin: 6px 0 0 24px; display: flex; align-items: flex-end; }
  .watering-note .fill-line { width: 90px; margin: 0 4px; }
  .service-promise {
    position: absolute; left: 30px; right: 30px; top: 284px;
    font-size: 8px; text-align: center; line-height: 1.35; color: var(--ink);
  }
  .contact-bar {
    position: absolute; left: 0; right: 0; bottom: 10px;
    display: flex; justify-content: center; gap: 16px;
    font-weight: 800; font-size: 11px; color: #1c3414;
  }
  /* ---------- Back ---------- */
  .back {
    left: 620px;
    background: var(--forest);
    color: var(--cream);
  }
  .sky-scene {
    position: absolute; left: 0; right: 0; top: 0; height: 148px;
    background: linear-gradient(180deg, var(--sky-top) 0%, #bcd0d8 55%, var(--sky-low) 100%);
  }
  .guidelines {
    position: absolute; left: 0; right: 0; top: 148px; bottom: 0;
    padding: 6px 18px 10px;
  }
  .guidelines-title {
    text-align: center; font-weight: 800; font-size: 10.5px;
    text-transform: uppercase; letter-spacing: .3px; margin-bottom: 5px;
  }
  .guide-columns { display: grid; grid-template-columns: 1fr 1fr; gap: 16px; }
  .guide-heading { font-weight: 800; font-size: 8px; text-transform: uppercase; margin-bottom: 2px; }
  .guide-text { font-size: 7.4px; line-height: 1.32; color: #e6e3b6; }
  .guide-list { list-style: none; }
  .guide-list li::before { content: "• "; }
</style>
</head>
<body>

<section class="card front" aria-label="Service call flyer, front">
  <div class="front-art" role="img" aria-label="Soft green flowing swirls and leaf shapes"></div>
  <div class="grass-strip" role="img" aria-label="Strip of green grass with white daisies"></div>

  <div class="brand">
    <span class="brand-dot"></span>
    <span class="brand-name">Fenwick<br>Turf Care</span>
  </div>

  <div class="service-stamp">
    <p class="stamp-date">Application time / date: <span class="fill-line"></span></p>
    <p class="stamp-title">Your lawn has been<br>proffesionally serviced today</p>
    <p class="stamp-by">By <span class="fill-line"></span></p>
  </div>

  <div class="application-panel">
    <h2 class="panel-title">Today's application consists of</h2>
    <ul class="treatment-list">
      <li class="treatment"><span class="check-box"></span><span>Seasonally Balanced Slow Release Fertilizer</span></li>
      <li class="treatment"><span class="check-box"></span><span>Broadleaf Weed Control<span class="treatment-note">(Please keep off the lawn until it is thoroughly dry)</span></span></li>
      <li class="treatment treatment-other"><span class="check-box"></span>Other <span class="fill-line"></span></li>
    </ul>
    <p class="watering-note">Please begin watering the lawn <span class="fill-line"></span> after application</p>
  </div>

  <p class="service-promise">We strive to complete work in a professional manner each and every visit. If you are not satisfied with the level of service you are receiving please contact us. We value your business and wish to maintain long-term relationships with our customers.</p>

  <p class="contact-bar">
    <span>Our phone number 604-918-4471</span>
    <span>Our Email address fenwickturfcare@mailora.net</span>
  </p>
</section>

<section class="card back" aria-label="Service call flyer, back">
  <div class="sky-scene" role="img" aria-label="Silhouettes of four trees through the seasons against a blue to pale yellow sky"></div>

  <div class="guidelines">
    <h2 class="guidelines-title">For best results please follow these general guidelines</h2>
    <div class="guide-columns">
      <div class="guide-column">
        <h3 class="guide-heading">Watering your lawn</h3>
        <div class="guide-text">
          <p>When rainfall is not sufficient to meet your lawns watering needs, follow these guidelines for a lush green lawn</p>
          <ul class="guide-list">
            <li>Your lawn requires approx. 1 - 1.5 inches of water per week, sometimes more in hot, dry weather</li>
            <li>Avoid short, frequent watering. It is best to water deeply once every 5 - 7 days. This encourages deep root growth</li>
            <li>You can use a flying disc or an empty tuna can to measure the amount you have watered. Just place it in the path of the sprinkler and when it is full, move your sprinkler to a new location</li>
            <li>Aerating your lawn once a year will help your lawn utilize more water and prevent unnecessary runoff</li>
          </ul>
        </div>
      </div>
      <div class="guide-column">
        <h3 class="guide-heading">Mowing your lawn</h3>
        <div class="guide-text">
          <p>Mowing your lawn properly can make all the difference in how it looks throughout the year</p>
          <ul class="guide-list">
            <li>You should mow your lawn at 2.5 - 3 inches (no shorter). Mowing at this length helps shade your roots and provides more leaf surface for your lawn to manufacture its own food. As an added bonus it will help your lawn retain its moisture and reduce watering requirements.</li>
            <li>As a general rule, try not to remove more then 1/3 of the leave blade in a single mowing. During periods of heavy growth, this may mean mowing more frequently then usual.</li>
            <li>Always ensure your lawn mower is maintained and the blade is sharp so that is cuts cleanly</li>
            <li>Your last mowing in the fall should be shorter about 2 inches</li>
          </ul>
        </div>
      </div>
    </div>
  </div>
</section>

</body>
</html>
```